Redesign of SnapHarbor Lumora Mobile app

The App exists, is up and running but the design is not the best (my creation and i am a developer).
Project landing page http://snapharbor.example/

Also the app has live tiles small, medium and large.

The purpose of this is to have a professional design and make this app the best app on the Lumora Mobile marketplace of his kind.

This app is a picture library that tells you where you've made you're pictures and gives you a unique perspective on the places that you have visited.

If this is successful there will be a version for Lumora 8, Zentrix and QOS also.

The app right now is for LM7 and LM8 and because of this the performance is not the best. With this new design the app will be for LM8 only and have the best performance possible.

I am not sure what else should i mention here but i am glad to answer to any questions if you are interested.

I am using Vantor draft as a design tool and Vantor Mixer and Crafton bench as development tools so if you can provide compatible file the better but is not mandatory.

It wold be nice to keep the existing color palette but again nothing is mandatory I just need a good design.

Links:
App on Marketplace http://www.appdepotmobile.example/en-us/store/app/snapharbor/7a3f9d21-0b6c-4e8d-9f12-ab34cd56ef78

App landing page http://snapharbor.example/
Updates

Reason: The submission time was extended doe to the request of designers.

We can do better, I will increase the budget with 200$  so the total budget will be 480$ so please consider this more seriously.

Thank you.

Target Market(s)

Lumora Mobile users that travel and make pictures.

Industry/Entity Type

Library

Requirements
Must have
• Panorama control as the App main page like in the present.

Representation of visited locations , Live tiles, Map, share location and picture..

If the designer comes up with better proposition they will be take in consideration.

None of these are mandatory but we should keep a connection with the present design so the users will not have the impression that this is a totally different app, this is SnapHarbor but better, more professional.

```html
<!DOCTYPE html>
<html lang="en">
<head>
<meta charset="utf-8">
<title>SnapHarbor – Locations</title>
<link rel="stylesheet" href="https://fonts.googleapis.com/css2?family=Open+Sans:wght@300;400&display=swap">
<style>
  :root {
    --page-bg: #f1f1f1;
    --ink: #161616;
    --ink-faded: rgba(40, 60, 30, 0.18);
    --accent: #2d9be0;
    --caption: #ffffff;
    --card: #ffffff;
    --card-edge: rgba(0, 0, 0, 0.28);
    --hill-sky: #d5e0c2;
    --hill-light: #a9bf82;
    --hill-mid: #7fa04f;
    --hill-deep: #557d33;
  }
  * { box-sizing: border-box; margin: 0; padding: 0; }
  html, body {
    width: 1200px; height: 1000px; overflow: hidden;
    background: var(--page-bg);
    font-family: "Open Sans", "Segoe UI", sans-serif;
  }
  .app-screen {
    position: absolute; left: 318px; top: 32px;
    width: 564px; height: 936px; overflow: hidden;
    color: var(--ink);
  }
  .app-backdrop {
    position: absolute; inset: 0;
    background:
      radial-gradient(ellipse 60% 30% at 70% 55%, rgba(140,175,90,0.55), transparent 70%),
      radial-gradient(ellipse 40% 25% at 20% 70%, rgba(70,100,45,0.5), transparent 70%),
      linear-gradient(180deg, var(--hill-sky) 0%, var(--hill-light) 28%, var(--hill-mid) 58%, var(--hill-deep) 100%);
  }
  .app-title {
    position: absolute; left: 18px; top: 6px;
    font-weight: 300; font-size: 104px; line-height: 1.2;
    letter-spacing: -2px; white-space: nowrap;
  }
  .pivot-headers {
    position: absolute; left: 26px; top: 148px;
    display: flex; gap: 30px;
    font-weight: 300; font-size: 48px; white-space: nowrap;
  }
  .pivot-item { color: var(--ink-faded); }
  .pivot-item.is-active { color: var(--accent); }

  .location {
    position: absolute; left: 0; width: 564px;
  }
  .photo-stack { position: absolute; left: 22px; top: 0; width: 272px; height: 210px; }
  .stack-card {
    position: absolute; inset: 0;
    background: var(--card);
    box-shadow: 0 2px 6px var(--card-edge);
  }
  .stack-card.back-one { transform: rotate(-3deg) translate(-4px, 4px); }
  .stack-card.back-two { transform: rotate(2.5deg) translate(6px, -2px); }
  .stack-card.front { padding: 7px; }
  .stack-photo { width: 100%; height: 100%; }
  .photo-tuscany { background: linear-gradient(160deg, #dfe9f3 0%, #b9a27a 35%, #e0b52a 55%, #9a5a3c 80%, #c98d6a 100%); }
  .photo-coast { background: linear-gradient(180deg, #4f8fd8 0%, #9dc4ea 35%, #e8e2d2 50%, #2aa5b0 72%, #0c6d7c 100%); }
  .photo-paris { background: linear-gradient(180deg, #cfd9e8 0%, #eef2f6 40%, #7c7466 62%, #6d8a4a 85%, #4b6a32 100%); }

  .location-count {
    position: absolute; right: 26px;
    font-weight: 300; font-size: 46px; line-height: 1;
    white-space: nowrap;
  }
  .location-place {
    position: absolute; right: 30px;
    font-weight: 300; font-size: 31px; line-height: 1;
    color: var(--caption); white-space: nowrap;
  }
</style>
</head>
<body>
  <main class="app-screen">
    <div class="app-backdrop" role="img" aria-label="Soft-focus photo of green rolling Tuscan hills with cypress trees"></div>

    <h1 class="app-title">SnapHarbor</h1>

    <nav class="pivot-headers">
      <span class="pivot-item">Recent</span>
      <span class="pivot-item is-active">Locations</span>
      <span class="pivot-item">Map</span>
    </nav>

    <section class="location" style="top:244px; height:210px;">
      <div class="photo-stack">
        <div class="stack-card back-one"></div>
        <div class="stack-card back-two"></div>
        <div class="stack-card front">
          <div class="stack-photo photo-tuscany" role="img" aria-label="Yellow vintage car on a brick street in a Tuscan hill town"></div>
        </div>
      </div>
      <div class="location-count" style="top:104px;">24 Photos</div>
      <div class="location-place" style="top:160px;">Tuscany, Italy</div>
    </section>

    <section class="location" style="top:506px; height:210px;">
      <div class="photo-stack">
        <div class="stack-card back-one"></div>
        <div class="stack-card back-two"></div>
        <div class="stack-card front">
          <div class="stack-photo photo-coast" role="img" aria-label="White rock formations rising from turquoise sea"></div>
        </div>
      </div>
      <div class="location-count" style="top:96px;">65 Photos</div>
      <div class="location-place" style="top:152px;">Athens, Greece</div>
    </section>

    <section class="location" style="top:752px; height:210px;">
      <div class="photo-stack">
        <div class="stack-card back-one"></div>
        <div class="stack-card back-two"></div>
        <div class="stack-card front">
          <div class="stack-photo photo-paris" role="img" aria-label="Eiffel Tower seen across a park under a pale sky"></div>
        </div>
      </div>
      <div class="location-count" style="top:86px;">+99 Photos</div>
      <div class="location-place" style="top:144px;">Paris, France</div>
    </section>
  </main>
</body>
</html>
```